design a web site for equipment and software pos company

We would a web site similar to the site we whited labed our rbts system .https://tryvelko.com/
website would be on RbTillSystems.com
we would a contact page
877-555-0148

We do not want an exact copy just something similar .
we are tablet po system

we are at

we are selling hardware and software

rb till systems
41 cedar hollow ln
linford, nj 07388
we are cloud based system

Target Market(s)

any retail merchant

Industry/Entity Type

credit card processing in POS asystems

Coding

Coded - Design and coding required

Number of Pages Required

5+ page

Requirements
Must have
• be able to connect webnarra hosting
Nice to have
• modern looking site
Should not have
• any red

```html
<!DOCTYPE html>
<html lang="en">
<head>
<meta charset="utf-8">
<title>RB Till Systems</title>
<link href="https://fonts.googleapis.com/css2?family=Frank+Ruhl+Libre:wght@400;700;900&family=Oswald:wght@400;500;600&family=Poppins:wght@400;500;600&display=swap" rel="stylesheet">
<style>
:root{
  --yellow:#f1c515;
  --black:#000;
  --dark:#161616;
  --text:#222;
  --white:#fff;
}
*{margin:0;padding:0;box-sizing:border-box}
html,body{width:1200px;height:2857px;overflow:hidden;background:#fff}
body{font-family:"Poppins",sans-serif;color:var(--text);position:relative}
.serif{font-family:"Frank Ruhl Libre",serif}
section,header,footer{position:absolute;left:0;width:1200px}
.abs{position:absolute}
.btn{position:absolute;background:var(--yellow);color:#111;font-family:"Oswald",sans-serif;font-weight:500;font-size:12px;border-radius:20px;display:flex;align-items:center;justify-content:center;text-transform:uppercase}

.hero{top:0;height:508px;background:var(--black);overflow:hidden}
.hero-photo{position:absolute;right:0;top:133px;width:640px;height:375px;background:linear-gradient(90deg,#000 0%,#3a3632 18%,#8b8580 50%,#b9b2a8 75%,#8d7b63 100%)}
.topbar{position:absolute;left:0;top:0;width:440px;height:32px;background:#1b1b1b;clip-path:polygon(0 0,100% 0,96% 100%,0 100%);color:#fff;font-size:12px;padding:8px 0 0 150px}
.logo{position:absolute;left:151px;top:56px;color:#fff;display:flex;align-items:center;gap:8px}
.logo .mark{width:44px;height:44px;border:2px solid var(--yellow);border-radius:50%}
.logo .name{font-family:"Frank Ruhl Libre",serif;font-size:30px;line-height:1}
.contact-top{position:absolute;top:24px;color:#fff;font-size:12px;line-height:1.2}
.contact-top b{font-family:"Oswald",sans-serif;font-weight:500;display:block}
.nav{position:absolute;left:480px;top:81px;width:720px;height:51px;background:var(--yellow);border-radius:26px 0 0 26px;display:flex;align-items:center;padding-left:38px}
.nav a{font-family:"Oswald",sans-serif;font-weight:500;font-size:12px;color:#111;text-decoration:none;width:115px}
.hero-text{position:absolute;left:151px;top:224px;color:#fff}
.hero-text .kicker{color:var(--yellow);font-size:24px}
.hero-text h1{font-size:46px;font-weight:400;line-height:1.1}
.hero-text p{font-size:12px;width:360px;margin-top:16px;line-height:1.35}
.arrow{position:absolute;width:64px;height:58px;border-radius:29px;display:flex;align-items:center;justify-content:center}

.welcome{top:508px;height:385px;background:#fff;overflow:hidden}
.tag{position:absolute;background:#111;color:var(--yellow);border-radius:16px;font-family:"Frank Ruhl Libre",serif;font-size:17px;padding:2px 16px}
.welcome h2{position:absolute;left:151px;top:76px;font-family:"Frank Ruhl Libre",serif;font-weight:700;font-size:50px;color:#111}
.welcome p{position:absolute;left:151px;top:142px;width:515px;font-size:12.2px;line-height:1.42;text-align:justify;color:#333;z-index:1}
.blob{position:absolute;left:650px;top:130px;width:232px;height:232px;border-radius:50%;background:#e2e2e2}
.frame{position:absolute;left:773px;top:51px;width:276px;height:272px;background:#fff;box-shadow:0 2px 8px rgba(0,0,0,.35);padding:8px}
.frame div{width:100%;height:100%;background:linear-gradient(160deg,#6e86a6 0%,#a7b4c2 40%,#3d4756 100%)}

.biz{top:893px;height:507px;background:var(--black);overflow:hidden}
.biz .divider{position:absolute;left:592px;top:0;width:8px;height:507px;background:#fff}
.biz .tab{position:absolute;left:0;top:23px;width:405px;height:74px;background:var(--yellow);border-radius:0 37px 37px 0;font-family:"Frank Ruhl Libre",serif;font-weight:700;font-size:31px;color:#111;padding:18px 0 0 148px}
.product{position:absolute;left:411px;top:71px;width:372px;height:372px;border-radius:50%;background:var(--yellow);display:flex;flex-direction:column;align-items:center;justify-content:center}
.product::before{content:"";position:absolute;inset:20px;border:2px dashed #fff;border-radius:50%}
.product .s{font-family:"Frank Ruhl Libre",serif;font-size:32px;color:#111}
.product .b{font-family:"Oswald",sans-serif;font-weight:600;font-size:56px;color:#111;line-height:1;letter-spacing:-1px}
.bt{position:absolute;width:120px;text-align:center;color:#fff;font-family:"Oswald",sans-serif;font-size:12px}
.bt .ic{width:80px;height:80px;margin:0 auto 16px;border:2px solid var(--yellow);border-radius:50%;display:flex;align-items:center;justify-content:center}

.pos{top:1400px;height:554px;background:linear-gradient(160deg,#d0cdcf,#c3c0c2 60%,#cbc8ca)}
.pos h2{position:absolute;left:0;width:1200px;top:55px;text-align:center;font-family:"Frank Ruhl Libre",serif;font-weight:700;font-size:70px;color:#111;line-height:1}
.pos p{position:absolute;left:0;width:1200px;top:134px;text-align:center;font-family:"Frank Ruhl Libre",serif;font-size:15px;color:#333;line-height:1.2}

.cta{top:1954px;height:161px;background:var(--yellow)}
.cta .t1{position:absolute;left:151px;top:44px;font-family:"Frank Ruhl Libre",serif;font-weight:700;font-size:19px;color:#111}
.cta .t2{position:absolute;left:151px;top:61px;font-family:"Frank Ruhl Libre",serif;font-weight:700;font-size:37px;color:#111}
.cta .t3{position:absolute;left:152px;top:109px;font-family:"Frank Ruhl Libre",serif;font-size:16px;color:#111}
.cta .sep{position:absolute;left:662px;top:54px;width:2px;height:62px;background:#c9a200}
.call{position:absolute;left:803px;top:55px;width:201px;height:44px;background:#111;border-radius:22px;color:#fff;font-family:"Oswald",sans-serif;font-size:13px;display:flex;align-items:center}
.call .ph{width:46px;height:44px;background:#fff;border-radius:50%;display:flex;align-items:center;justify-content:center;margin-right:14px}

.partners{top:2115px;height:405px;background:#fff}
.partners h2{position:absolute;left:0;width:1200px;top:90px;text-align:center;font-family:"Frank Ruhl Libre",serif;font-weight:700;font-size:68px;color:#111}
.logos{position:absolute;left:151px;top:190px;display:flex;gap:5px}
.logos div{width:146px;height:123px;border:1px solid #cfcfcf;display:flex;align-items:center;justify-content:center;font-size:17px;font-weight:500;color:#111}
.circ{position:absolute;width:33px;height:33px;border:1px solid #333;border-radius:50%;display:flex;align-items:center;justify-content:center}

.footer{top:2520px;height:337px;background:var(--dark)}
.f-strip{position:absolute;left:151px;top:2479px;width:224px;height:18px;background:var(--yellow);clip-path:polygon(0 0,100% 0,94% 100%,0 100%)}
.f-box{position:absolute;left:151px;top:2495px;width:260px;height:362px;background:#000;color:#fff;padding:38px 0 0 26px;font-size:11px;line-height:1.55}
.f-box p{width:215px;margin-top:14px}
.social{display:flex;gap:7px;margin-top:22px}
.social span{width:38px;height:38px;border:1px dashed #fff;border-radius:50%}
.f-title{position:absolute;top:54px;font-size:22px;font-weight:600;color:#fff}
.f-title span{color:var(--yellow)}
.f-title::after{content:"";position:absolute;left:0;top:36px;width:40px;height:3px;background:var(--yellow)}
.f-links{position:absolute;left:480px;top:102px;display:grid;grid-template-columns:148px 140px;row-gap:26px;font-size:12px;color:#fff}
.f-links span::before{content:"--";margin-right:12px}
.f-contact{position:absolute;left:814px;top:100px;color:#fff;font-size:12px;line-height:1.3}
.f-contact .row{display:flex;gap:14px;margin-bottom:20px}
.f-contact b{font-weight:600}
.copy{position:absolute;left:480px;top:282px;width:720px;height:55px;background:var(--yellow);border-radius:28px 0 0 0;font-size:12px;color:#111;padding:24px 0 0 50px}
</style>
</head>
<body>

<header class="hero">
  <div class="hero-photo" role="img" aria-label="Photo of a cashier processing a card payment at a tablet POS terminal"></div>
  <div class="topbar">Working Hours : Mon-Sat:9.30am To 7.00pm</div>
  <div class="logo"><div class="mark"></div><div class="name">RB Till<br>Systems</div></div>
  <div class="contact-top" style="left:485px">
    <svg class="abs" style="left:0;top:0" width="28" height="30" viewBox="0 0 28 30" fill="none" stroke="#f1c515" stroke-width="2"><rect x="2" y="10" width="24" height="18"/><path d="M2 10l12 10 12-10M6 10V2h16v8"/></svg>
    <div style="margin-left:38px"><b>SEND YOUR MAIL AT</b>info@rbtillsystems.com</div>
  </div>
  <div class="contact-top" style="left:722px">
    <svg class="abs" style="left:0;top:0" width="22" height="28" viewBox="0 0 22 28" fill="none" stroke="#f1c515" stroke-width="2"><path d="M11 26S2 15 2 10a9 9 0 0118 0c0 5-9 16-9 16z"/><circle cx="11" cy="10" r="3"/></svg>
    <div style="margin-left:32px"><b>RB TILL SYSTEMS</b>41 cedar hollow ln linford,<br>&nbsp;nj 07388</div>
  </div>
  <div class="btn" style="left:955px;top:21px;width:93px;height:29px">Get Started</div>
  <nav class="nav"><a>HOME</a><a style="width:84px">ABOUT</a><a style="width:123px">BUSINESS TYPES</a><a style="width:97px">PRODUCTS</a><a style="width:92px">PARTNERS</a><a>WHITE LABEL</a></nav>
  <div class="hero-text">
    <div class="kicker serif">Best of</div>
    <h1 class="serif">Rb Till systems</h1>
    <p>Lorem ipsum dolor sit amet, consectetur adipiscing elit. Mauris accumsan elementum varius. Nulla ullamcorper auctor accumsan. Ut enim nulla, mattis quis .</p>
  </div>
  <div class="btn" style="left:154px;top:394px;width:87px;height:32px">Read More</div>
  <div class="arrow" style="left:-6px;top:248px;background:#3a3a3a"><svg width="14" height="20" viewBox="0 0 14 20" fill="none" stroke="#fff" stroke-width="2.5"><path d="M11 2L3 10l8 8"/></svg></div>
  <div class="arrow" style="left:1145px;top:248px;background:var(--yellow)"><svg width="14" height="20" viewBox="0 0 14 20" fill="none" stroke="#111" stroke-width="2.5"><path d="M3 2l8 8-8 8"/></svg></div>
</header>

<section class="welcome">
  <div class="tag" style="left:149px;top:49px">Welcome to</div>
  <h2>RB TILL SYSTEMS</h2>
  <p>Lorem ipsum dolor sit amet, consectetur adipiscing elit. Mauris accumsan elementum varius. Nulla ullamcorper auctor accumsan. Ut enim nulla, mattis quis consequat ut, dapibus sed diam. Duis non lobortis ligula. Phasellus congue ipsum nec malesuada maximus. Fusce non lorem quis dolor consectetur pretium vitae ac est. Vestibulum auctor luctus erat.aliquet. Mauris vitae felis vitae dolor suscipit porta. congue ipsum nec malesuada maximus. Fusce non lorem quis dolor consectetur pretium vitae ac est. Vestibulum auctor luctus erat.aliquet.</p>
  <div class="btn" style="left:151px;top:293px;width:98px;height:33px;box-shadow:1px 2px 0 #111">Read More</div>
  <div class="blob"></div>
  <div class="frame"><div role="img" aria-label="Photo of a touchscreen POS terminal with card reader on a store counter"></div></div>
</section>

<section class="biz">
  <div class="divider"></div>
  <div class="tab">BUSINESS TYPE</div>
  <div class="product"><div class="s">Perfect solution</div><div class="b">OUR PRODUCT</div></div>
  <div class="bt" style="left:130px;top:145px"><div class="ic"><svg width="36" height="36" viewBox="0 0 36 36" fill="none" stroke="#f1c515" stroke-width="2.5"><rect x="5" y="12" width="26" height="20" rx="2"/><path d="M12 12V8a6 6 0 0112 0v4"/></svg></div>SHOPPING</div>
  <div class="bt" style="left:268px;top:145px"><div class="ic"><svg width="38" height="36" viewBox="0 0 38 36" fill="none" stroke="#f1c515" stroke-width="2.5"><path d="M5 24a14 14 0 0128 0zM2 27h34M19 7v3"/><circle cx="19" cy="6" r="2"/></svg></div>RESTURANT</div>
  <div class="bt" style="left:813px;top:145px"><div class="ic"><svg width="30" height="40" viewBox="0 0 30 40" fill="none" stroke="#f1c515" stroke-width="2.5"><circle cx="15" cy="12" r="9"/><path d="M6 16l9 22 9-22"/></svg></div>ICE FACTORY</div>
  <div class="bt" style="left:948px;top:145px"><div class="ic"><svg width="40" height="36" viewBox="0 0 40 36" fill="none" stroke="#f1c515" stroke-width="2.5"><circle cx="9" cy="28" r="5"/><circle cx="31" cy="28" r="5"/><path d="M9 28h22l-4-12h-9M26 10h10v10H26z"/></svg></div>DELIVERY</div>
  <div class="bt" style="left:130px;top:296px"><div class="ic"><svg width="38" height="36" viewBox="0 0 38 36" fill="none" stroke="#f1c515" stroke-width="2.5"><path d="M4 4h30l2 8H2zM4 12v20h30V12M10 32V20h8v12M22 20h8v6h-8z"/></svg></div>SHOP</div>
  <div class="bt" style="left:268px;top:296px"><div class="ic"><svg width="40" height="36" viewBox="0 0 40 36" fill="none" stroke="#f1c515" stroke-width="2.5"><path d="M3 32V16l9 6v-6l9 6v-6l9 6V6h6v26zM8 26h4M18 26h4M28 26h4"/></svg></div>FACTORY</div>
  <div class="bt" style="left:813px;top:296px"><div class="ic"><svg width="40" height="36" viewBox="0 0 40 36" fill="none" stroke="#f1c515" stroke-width="2.5"><path d="M4 16a16 10 0 0132 0zM3 20h34M5 24h30v4a4 4 0 01-4 4H9a4 4 0 01-4-4z"/></svg></div>FOOD</div>
  <div class="bt" style="left:948px;top:296px"><div class="ic"><svg width="44" height="12" viewBox="0 0 44 12" fill="#f1c515"><circle cx="6" cy="6" r="5"/><circle cx="22" cy="6" r="5"/><circle cx="38" cy="6" r="5"/></svg></div>BUSINESS TYPE</div>
</section>

<section class="pos">
  <h2>POS</h2>
  <p>THOUSAND OF FREE FEATURES WITHOUT HAVING TO<br>DOWNLOAD ANY 3RD PARTY APPS.</p>
  <svg class="abs" style="left:0;top:0" width="1200" height="554" viewBox="0 0 1200 554">
    <defs><marker id="ah" markerWidth="10" markerHeight="10" refX="8" refY="5" orient="auto"><path d="M0 0L10 5 0 10z" fill="#222"/></marker></defs>
    <g stroke="#444" stroke-width="3" fill="none" marker-end="url(#ah)">
      <line x1="441" y1="276" x2="550" y2="276"/>
      <line x1="667" y1="276" x2="776" y2="276"/>
      <line x1="826" y1="332" x2="774" y2="416"/>
      <line x1="673" y1="443" x2="556" y2="443"/>
      <line x1="485" y1="390" x2="411" y2="310"/>
    </g>
    <circle cx="380" cy="276" r="52" fill="#f1c515"/>
    <g fill="#fff" stroke="#f1c515" stroke-width="3">
      <circle cx="606" cy="276" r="52"/><circle cx="832" cy="276" r="52"/>
      <circle cx="500" cy="443" r="52"/><circle cx="726" cy="443" r="52"/>
    </g>
    <g fill="none" stroke="#333" stroke-width="2.2">
      <rect x="358" y="258" width="44" height="30" rx="2"/><path d="M372 296h16M380 288v8M366 266h4l4 12h16l3-9h-20"/>
      <rect x="584" y="280" width="44" height="14"/><path d="M586 268h18v8h-18zM612 270a6 6 0 0112 0v6h-12z"/><circle cx="618" cy="260" r="5"/>
      <rect x="810" y="256" width="44" height="26"/><path d="M816 264h14M816 272h20M816 282v16h12v-16"/>
      <path d="M478 460h18l10-8h14M480 440l4-16 14 4-4 16zM500 420h22v28h-22z"/><circle cx="511" cy="430" r="4"/>
      <path d="M702 432h32v22h-32zM734 440h10l6 8v6h-16"/><circle cx="712" cy="456" r="4"/><circle cx="740" cy="456" r="4"/><path d="M712 442l5 5 9-9"/>
    </g>
  </svg>
</section>

<section class="cta">
  <div class="t1">BETTER SOFTWARE</div>
  <div class="t2">FOR A BETTER BUSINESS</div>
  <div class="t3">The Only Software You Need, Moving Your Business Forward.</div>
  <div class="sep"></div>
  <div class="call"><div class="ph"><svg width="24" height="24" viewBox="0 0 24 24" fill="none" stroke="#333" stroke-width="1.8"><path d="M5 3l4 1 2 5-3 2a12 12 0 005 5l2-3 5 2 1 4-3 2C10 21 3 14 3 6z"/></svg></div>CALL US&nbsp;&nbsp;(855) 555-0192</div>
</section>

<section class="partners">
  <div class="tag" style="left:520px;top:58px;font-size:16px;padding:3px 17px">OUR PARTNERS</div>
  <h2>LOVE US</h2>
  <div class="circ" style="left:82px;top:232px"><svg width="10" height="14" viewBox="0 0 10 14" fill="none" stroke="#111" stroke-width="2"><path d="M8 2L3 7l5 5"/></svg></div>
  <div class="logos">
    <div>Paymoria</div><div>Pearwood</div><div>Vexa</div><div>Crispden</div><div>Brightnook</div><div>Softwick</div>
  </div>
  <div class="circ" style="left:1081px;top:232px"><svg width="10" height="14" viewBox="0 0 10 14" fill="none" stroke="#111" stroke-width="2"><path d="M2 2l5 5-5 5"/></svg></div>
</section>

<footer class="footer">
  <div class="f-title" style="left:480px">Useful <span>Links</span></div>
  <div class="f-links">
    <span>HOME</span><span>PARTNERS</span><span>ABOUT</span><span>WHITE LABEL</span><span>BUSINESS TYPES</span><span>CONTACT US</span><span>PRODUCTS</span>
  </div>
  <div class="f-title" style="left:814px">Contact <span>Us</span></div>
  <div class="f-contact">
    <div class="row"><svg width="22" height="28" viewBox="0 0 22 28" fill="none" stroke="#f1c515" stroke-width="2"><path d="M11 26S2 15 2 10a9 9 0 0118 0c0 5-9 16-9 16z"/><circle cx="11" cy="10" r="3"/></svg><div>Rb till systems<br>41 cedar hollow ln linford, nj 07388</div></div>
    <div class="row"><svg width="26" height="28" viewBox="0 0 28 30" fill="none" stroke="#f1c515" stroke-width="2"><rect x="2" y="10" width="24" height="18"/><path d="M2 10l12 10 12-10M6 10V2h16v8"/></svg><div><b>SEND YOUR MAIL AT</b><br>info@rbtillsystems.com</div></div>
    <div class="row"><svg width="26" height="28" viewBox="0 0 26 28" fill="none" stroke="#f1c515" stroke-width="2"><circle cx="13" cy="15" r="10"/><path d="M13 9v6l4 3M3 5l5-3M23 5l-5-3"/></svg><div><b>WORKING HOURS</b><br>Mon-Sat:9.30am To 7.00pm</div></div>
  </div>
  <div class="copy">© 2021 RB TILL SYSTEMS. ALL RIGHT RESERVED.</div>
</footer>
<div class="f-strip"></div>
<div class="f-box">
  <div style="display:flex;align-items:center;gap:8px"><div style="width:30px;height:30px;border:2px solid #f1c515;border-radius:50%"></div><div class="serif" style="font-size:20px;line-height:1">RB Till<br>Systems</div></div>
  <p>Tillora is an exclusive multi-purpose 100% responsive Template Theme with powerful features.</p>
  <p>Simple and well-structured coding, high quality and flexible layout, scalable features along with color schemes to create tailor-cut websites.</p>
  <div class="social"><span></span><span></span><span></span><span></span></div>
</div>

</body>
</html>
```